IT Company Business Card Rebranding

We want to modernize our business cards massively. We want to incorporate aspects of our old business card such as the white and geometric design with the blues of another icon. Existing Logo, old business card and icon are all attached.

We are a modern IT company that provides support for new and growing technologies and want our business cards to be modern yet professional.
Updates

Note: Do not use file ICON.png in design. This is just a design we like Added Wednesday, March 9, 2016

Industry/Entity Type

Information Technology

Contact Information for Business Card

Roughly 43 : 26 or 1075 x 650 px

Font styles to use
Serif

Colors
0492cd
3276b5
33a6d7
86cfc6
cfeae6
cee9f5
ffffff

Requirements
Must have
• Modern yet professional
Nice to have
• We would like to incorporate the blues of our existing logo and of the icon provided. Really like the design of the icon.
Should not have
• Too Decorative. Just simple and professional.
• Not have the circle icon, as it is a copyrighted icon, I just like the colors and the geometric design

```html
<!DOCTYPE html>
<html lang="en">
<head>
<meta charset="utf-8">
<title>Corvex IT – Business Card</title>
<link rel="stylesheet" href="https://fonts.googleapis.com/css2?family=Open+Sans:wght@400;600&display=swap">
<style>
  :root {
    --page-bg: #ece9e6;
    --card-grey: #e4e4e4;
    --facet-light: #f4f4f4;
    --facet-mid: #d6d6d6;
    --blue-top: #1fa2ef;
    --blue-bottom: #1232c4;
    --wordmark-grey: #8a8a8a;
    --white: #ffffff;
  }
  * { margin: 0; padding: 0; box-sizing: border-box; }
  html, body {
    width: 1200px; height: 900px; overflow: hidden;
    background: var(--page-bg);
    font-family: "Open Sans", Arial, sans-serif;
  }
  .canvas { position: relative; width: 1200px; height: 900px; }

  .card {
    position: absolute;
    background: var(--card-grey);
    overflow: hidden;
    box-shadow: 0 6px 18px rgba(0,0,0,0.18);
  }
  .card--front { left: 78px; top: 33px; width: 587px; height: 365px; }
  .card--back  { left: 388px; top: 505px; width: 567px; height: 352px; }

  .facet-band {
    position: absolute; left: 0; top: 0; width: 100%;
    background: linear-gradient(180deg, var(--facet-light) 0%, var(--facet-mid) 55%, var(--card-grey) 100%);
  }
  .card--front .facet-band { height: 100px; }
  .card--back .facet-band { height: 85px; }

  .wordmark {
    position: absolute;
    font-weight: 400;
    letter-spacing: 0.32em;
    text-transform: uppercase;
    white-space: nowrap;
  }
  .card--front .wordmark {
    left: 30px; top: 146px;
    font-size: 24px; color: var(--wordmark-grey);
  }

  .blue-band {
    position: absolute; left: 0; width: 100%;
    background: linear-gradient(180deg, var(--blue-top) 0%, var(--blue-bottom) 100%);
    color: var(--white);
  }
  .card--front .blue-band { top: 200px; height: 165px; padding: 16px 0 0 32px; }
  .card--back .blue-band { top: 110px; height: 131px; display: flex; align-items: center; justify-content: center; }
  .card--back .wordmark { position: static; font-size: 27px; color: var(--white); letter-spacing: 0.4em; padding-left: 0.4em; }

  .person { font-size: 17px; line-height: 28px; }
  .person__name { font-weight: 600; font-size: 21px; }
  .person__role { font-size: 15px; }

  .contact-list { list-style: none; margin-top: 16px; }
  .contact-list li {
    display: flex; align-items: center; gap: 9px;
    font-size: 15px; line-height: 24.5px;
  }
  .contact-list svg { width: 12px; height: 12px; fill: var(--white); flex: none; }
</style>
</head>
<body>
<main class="canvas">

  <section class="card card--front" aria-label="Business card front">
    <div class="facet-band" role="img" aria-label="Light grey geometric faceted pattern"></div>
    <p class="wordmark">Corvex IT</p>
    <div class="blue-band">
      <p class="person"><span class="person__name">Marcus</span> - <span class="person__role">Technical Services</span></p>
      <ul class="contact-list">
        <li>
          <svg viewBox="0 0 24 24" aria-hidden="true"><path d="M6.6 10.8a15.1 15.1 0 0 0 6.6 6.6l2.2-2.2c.3-.3.7-.4 1-.2 1.1.4 2.3.6 3.6.6.6 0 1 .4 1 1V20c0 .6-.4 1-1 1A17 17 0 0 1 3 4c0-.6.4-1 1-1h3.5c.6 0 1 .4 1 1 0 1.3.2 2.5.6 3.6.1.3 0 .7-.2 1z"/></svg>
          (044)-555-0142
        </li>
        <li>
          <svg viewBox="0 0 24 24" aria-hidden="true"><path d="M2 5h20v14H2z M3.5 6.5 12 13l8.5-6.5" fill="none" stroke="#fff" stroke-width="2"/><path d="M2 5h20L12 12.5z"/></svg>
          hello@corvexit.com
        </li>
        <li>
          <svg viewBox="0 0 24 24" aria-hidden="true"><circle cx="12" cy="12" r="10"/><path d="M2 12h20M12 2c3 3 3 17 0 20M12 2c-3 3-3 17 0 20" fill="none" stroke="#1a5fd8" stroke-width="1.6"/></svg>
          www.corvexit.com
        </li>
      </ul>
    </div>
  </section>

  <section class="card card--back" aria-label="Business card back">
    <div class="facet-band" role="img" aria-label="Light grey geometric faceted pattern"></div>
    <div class="blue-band">
      <p class="wordmark">Corvex IT</p>
    </div>
  </section>

</main>
</body>
</html>
```